Vardel coatings banner

Banner same size Brisk Hallways advert banner
of previous one Brisk Hallways advert banner 215cm x 1055cm
but for a paint company, called Vardel Coatings.
I want the concept to be similar to the attached, i want to put some real drum paint in front of the banner concept to look in Harmony with your concept on the banner.
The company is specialized in producing and painting houses and offices indoor and outdoor and applying epoxy on floors..

```html
<!DOCTYPE html>
<html lang="en">
<head>
<meta charset="utf-8">
<title>Vardel Coatings Banner</title>
<link href="https://fonts.googleapis.com/css2?family=Arimo:wght@700&family=Fraunces:opsz,wght@9..144,700&display=swap" rel="stylesheet">
<style>
  :root {
    --bg-violet: #6a4fc4;
    --bg-blue: #4d6ad0;
    --bg-pink: #b05ec8;
    --bg-sky: #6f9be0;
    --brand-blue: #2f7bbd;
    --brand-mark: #1f5f93;
    --ink-dark: #3d3848;
    --ink-light: #ffffff;
    --outline-navy: #1d2a5c;
    --corner-disc: #c9cff5;
    --paint-blue: #2a56e0;
    --tin-grey: #a9b4bf;
  }
  html, body {
    margin: 0;
    padding: 0;
    width: 1200px;
    height: 251px;
    overflow: hidden;
  }
  .banner {
    position: relative;
    width: 1200px;
    height: 251px;
    overflow: hidden;
    background:
      radial-gradient(ellipse 420px 220px at 330px 250px, rgba(200, 90, 200, 0.55), transparent 70%),
      radial-gradient(ellipse 380px 200px at 720px 40px, rgba(140, 170, 230, 0.45), transparent 70%),
      linear-gradient(100deg, var(--bg-violet) 0%, var(--bg-pink) 35%, var(--bg-sky) 55%, var(--bg-violet) 78%, var(--bg-blue) 100%);
    font-family: "Arimo", Arial, sans-serif;
  }
  .corner-disc {
    position: absolute;
    border-radius: 50%;
    background: var(--corner-disc);
    opacity: 0.85;
  }
  .corner-disc--top-left { left: -22px; top: -22px; width: 44px; height: 44px; }
  .corner-disc--bottom-right { right: -32px; bottom: -26px; width: 64px; height: 64px; }
  .paint-cans {
    position: absolute;
    left: 8px;
    top: 24px;
    width: 315px;
    height: 222px;
    border-radius: 40px 40px 60px 30px;
    background:
      radial-gradient(ellipse 150px 50px at 190px 190px, var(--paint-blue), transparent 75%),
      linear-gradient(160deg, var(--tin-grey) 0%, #7fa8d8 45%, var(--paint-blue) 100%);
    opacity: 0.9;
  }
  .brand-dot {
    position: absolute;
    left: 346px;
    top: 18px;
    width: 128px;
    height: 128px;
    border-radius: 50%;
    background: var(--brand-mark);
  }
  .brand-name {
    position: absolute;
    left: 528px;
    top: 6px;
    margin: 0;
    color: var(--brand-blue);
    font-weight: 700;
    font-size: 66px;
    line-height: 70px;
    letter-spacing: -1.5px;
    text-transform: uppercase;
    white-space: nowrap;
  }
  .tagline {
    position: absolute;
    left: 328px;
    top: 156px;
    margin: 0;
    color: var(--ink-dark);
    font-weight: 700;
    font-size: 34px;
    letter-spacing: 0.3px;
    white-space: nowrap;
    text-shadow: 1px 1px 0 rgba(255, 255, 255, 0.45);
  }
  .services {
    position: absolute;
    left: 326px;
    top: 201px;
    margin: 0;
    color: var(--ink-light);
    font-family: "Fraunces", Georgia, serif;
    font-weight: 700;
    font-size: 22.5px;
    white-space: nowrap;
    text-shadow:
      1px 0 0 var(--outline-navy), -1px 0 0 var(--outline-navy),
      0 1px 0 var(--outline-navy), 0 -1px 0 var(--outline-navy),
      1px 1px 0 var(--outline-navy), -1px -1px 0 var(--outline-navy);
  }
</style>
</head>
<body>
  <section class="banner">
    <span class="corner-disc corner-disc--top-left"></span>
    <span class="corner-disc corner-disc--bottom-right"></span>

    <div class="paint-cans" role="img" aria-label="Two metal paint tins, one tipped over spilling bright blue paint"></div>

    <span class="brand-dot"></span>
    <h1 class="brand-name">Vardel<br>Coatings</h1>

    <p class="tagline">Transform Your Home with Vardel Coatings !!</p>
    <p class="services">Specializing in Indoor and Outdoor Painting, Epoxy Flooring, and More</p>
  </section>
</body>
</html>
```